Business Card Design Project (Beer industry)

I am seeking a redesign of my business card. I am looking for something that will really stand out in both texture and feel. Something more on the modern side then traditional. Nothing die cut shaped like a beer mug please.

The card is used mostly for other industry professionals, as well as bar and restaurant owners. My title is Strategy & Acquisitions. If you would like to somehow incorporate that theme, that may work.

My business is craft and imported beer. Nothing fizzy and yellow, so my products are more on the upscale side.
Updates

I was able to update my logo in .ai and .tif format. I hope that helps. 

Thank you all for your creative ideas. I have uploaded my current business card in pdf format, as well as our logo in .eps file format. We are excited about the submissions so far and want to thank you all again.

PS Please do not include fax number in future submissions, as we are looking for something more creative and a fax says 1999 and not 2015, which is the message we are going for, without being futuristic. 

Thank you all once again for all of your submissions. If we would consider a two sided card, we would like the opposite side not to be the same as the front. The styles we have seen so far, it appears the front and back are too similar. Again, a two sided card is not required. Thank you and we look forward to pushing the boundaries of your creativity. Cheers

Target Market(s)

My card would mostly go to bar and restaurant operators as well as other beer industry professionals

Industry/Entity Type

Restaurant

Requirements
Nice to have
• Two sided would be considered, although not required
Should not have
• Anything die cut shaped like a beer mug.

```html
<!DOCTYPE html>
<html lang="en">
<head>
<meta charset="utf-8">
<title>Harbor Cask – Business Card</title>
<link rel="stylesheet" href="https://fonts.googleapis.com/css2?family=Didact+Gothic&family=Questrial&display=swap">
<style>
  :root {
    --page: #f3ece2;
    --amber: #f6b436;
    --amber-soft: #fbd77e;
    --cream: #fdf4e0;
    --white: #ffffff;
    --navy: #1f3467;
    --wine: #8e1b1b;
    --gold: #fcd45a;
    --rust: #d9822b;
    --ink: #2a3a6e;
  }
  * { margin: 0; padding: 0; box-sizing: border-box; }
  html, body {
    width: 1200px; height: 1157px; overflow: hidden;
    background: var(--page);
    font-family: "Didact Gothic", "Questrial", sans-serif;
  }
  .card {
    position: absolute; left: 320px; top: 88px;
    width: 560px; height: 980px;
    border-radius: 40px; overflow: hidden;
    background: linear-gradient(180deg, var(--amber) 0%, var(--amber-soft) 22%, var(--cream) 45%, var(--white) 62%);
    box-shadow: 0 10px 30px rgba(80, 50, 10, 0.18);
  }
  .card-shapes { position: absolute; inset: 0; }
  .brand-art {
    position: absolute; left: 90px; top: 70px; width: 380px; height: 300px;
    border-radius: 18px;
    background: linear-gradient(180deg, #3a5699 0%, #2a4684 55%, #d9a83a 100%);
    opacity: 0.9;
  }
  .brand-name {
    position: absolute; left: 0; right: 0; top: 392px;
    text-align: center; font-size: 56px; letter-spacing: 2px;
    color: var(--wine);
  }
  .holder {
    position: absolute; left: 160px; top: 536px; width: 350px; text-align: center;
  }
  .holder-name { font-size: 30px; color: var(--gold); }
  .holder-title { font-size: 19px; color: var(--rust); margin-top: 4px; }
  .direct {
    position: absolute; left: 0; right: 40px; top: 672px;
    text-align: right; font-size: 24px; color: var(--ink); line-height: 1.35;
  }
  .direct .num { font-size: 28px; color: var(--wine); }
  .office {
    position: absolute; left: 40px; right: 40px; top: 800px;
    display: flex; justify-content: space-between; align-items: flex-start;
    font-size: 22px; color: var(--ink); line-height: 1.3;
  }
  .office-lines.right { text-align: right; }
  .site {
    position: absolute; left: 0; right: 0; top: 878px;
    text-align: center; font-size: 34px; color: var(--wine); letter-spacing: 0.5px;
  }
</style>
</head>
<body>
  <div class="card">
    <svg class="card-shapes" width="560" height="980" viewBox="0 0 560 980" aria-hidden="true">
      <polygon points="120,505 560,470 560,610 60,650" fill="var(--gold)"/>
      <polygon points="150,520 520,505 500,640 150,665" fill="var(--wine)"/>
      <polygon points="0,748 560,730 560,768 0,786" fill="var(--gold)"/>
      <rect x="0" y="930" width="560" height="50" fill="var(--navy)"/>
    </svg>

    <div class="brand-art" role="img" aria-label="Brand illustration: city skyline with a glass of beer and stars"></div>
    <div class="brand-name">Harbor Cask</div>

    <div class="holder">
      <div class="holder-name">Dan Whitlow</div>
      <div class="holder-title">Strategy &amp; Acquisitions</div>
    </div>

    <div class="direct">
      <div>Cell: <span class="num">(555) 214-0387</span></div>
      <div>Email: dan@harborcask.com</div>
    </div>

    <div class="office">
      <div class="office-lines">48 Pier Lane<br>Ashford, NY 10990</div>
      <div class="office-lines right">Phone: (555) 301-7720</div>
    </div>

    <div class="site">www.harborcask.com</div>
  </div>
</body>
</html>
```